Email Signature

We are looking for creative email signature for our company. Please find attached the logo of our company for your reference. now we understand there isn't much can be done with email signature but we are looking for out of the box designs. Nothing specific in mind

Please insert fake numbers, website and/or address, etc just to showcase the designs. once the design is chosen we will provide the actual details.
Updates

Dear All,

We wouldlike to extend our apology for not being able to provide feedbacks to everysingle design. We were extremely busy and we have multiple contests opensimultaneously which makes the process harder. However, thank you all for theefforts you have put into this contest. We have received anoverwhelming quality responses & it has been a very difficult task tochoose just one, we easily Loved at least several designs...

Thanksagain for participating, we wish you all success in your design ventures.

Kindregards,

KLC Team

Industry/Entity Type

It Company

```html
<!DOCTYPE html>
<html lang="en">
<head>
<meta charset="utf-8">
<title>TableTrade Email Signature</title>
<link href="https://fonts.googleapis.com/css2?family=Source+Sans+3:wght@400;700&display=swap" rel="stylesheet">
<style>
  :root {
    --brand-blue: #2f7fc2;
    --brand-green: #8cc63f;
    --ink: #3d3d3d;
    --rule: #d4d4d4;
    --paper: #ffffff;
  }
  * { margin: 0; padding: 0; box-sizing: border-box; }
  html, body { width: 1200px; height: 442px; overflow: hidden; background: var(--paper); }
  .signature {
    position: relative;
    width: 1200px;
    height: 442px;
    background: var(--paper);
    font-family: "Source Sans 3", "Myriad Pro", sans-serif;
    color: var(--ink);
    overflow: hidden;
  }
  .brand-name {
    position: absolute;
    left: 90px;
    top: 128px;
    font-size: 96px;
    font-weight: 700;
    line-height: 1;
    letter-spacing: -2px;
    color: var(--brand-blue);
  }
  .divider {
    position: absolute;
    left: 661px;
    top: 40px;
    width: 1px;
    height: 292px;
    background: var(--rule);
  }
  .contact {
    position: absolute;
    left: 697px;
    top: 40px;
  }
  .contact-name {
    font-size: 29px;
    font-weight: 700;
    color: var(--brand-blue);
    line-height: 36px;
  }
  .contact-title {
    font-size: 21px;
    line-height: 28px;
    margin-bottom: 10px;
  }
  .contact-list { list-style: none; }
  .contact-list li {
    display: flex;
    align-items: center;
    height: 39.5px;
    font-size: 22px;
  }
  .contact-list svg {
    width: 18px;
    height: 18px;
    margin-right: 13px;
    fill: var(--brand-blue);
  }
  .address {
    margin-top: 14px;
    font-size: 22px;
    line-height: 33px;
    font-style: normal;
  }
  .waves {
    position: absolute;
    left: 0;
    bottom: 0;
    width: 1200px;
    height: 442px;
  }
</style>
</head>
<body>
<div class="signature">
  <svg class="waves" viewBox="0 0 1200 442" preserveAspectRatio="none" aria-hidden="true">
    <path fill="var(--brand-green)" d="M0,307 C150,345 300,362 520,358 C800,352 1000,362 1200,396 L1200,399 C1000,370 800,366 520,372 C300,378 150,372 0,345 Z"/>
    <path fill="var(--brand-blue)" d="M0,356 C200,384 420,380 640,375 C880,370 1060,378 1200,402 L1200,442 L0,442 Z"/>
  </svg>

  <div class="brand-name">TableTrade</div>

  <div class="divider"></div>

  <div class="contact">
    <div class="contact-name">Your Name</div>
    <div class="contact-title">Title</div>
    <ul class="contact-list">
      <li>
        <svg viewBox="0 0 24 24"><path d="M12 1a11 11 0 1 0 0 22a11 11 0 0 0 0-22zm0 2a9 9 0 1 1 0 18a9 9 0 0 1 0-18zm-2.6 3.5l-1.6 1c-.8.6-.9 2.3.4 4.8 1.4 2.6 3 3.8 4 3.6l1.7-.9-1.6-2.6-1.1.6c-.5-.2-1.4-1.6-1.5-2.2l1-.7z"/></svg>
        123-456-7890
      </li>
      <li>
        <svg viewBox="0 0 24 24"><path d="M7 3h8l2 2v4H7zM3 10h18a1 1 0 0 1 1 1v7a1 1 0 0 1-1 1h-1v2h-3v-2H7v2H4v-2H3a1 1 0 0 1-1-1v-7a1 1 0 0 1 1-1z"/></svg>
        123-456-7890
      </li>
      <li>
        <svg viewBox="0 0 24 24"><path d="M12 1a11 11 0 1 0 0 22a11 11 0 0 0 0-22zm-1 2.1V7H8.2c.6-2 1.6-3.4 2.8-3.9zm2 0c1.2.5 2.2 1.9 2.8 3.9H13zM8.6 3.8C8 4.7 7.5 5.8 7.2 7H4.9a9 9 0 0 1 3.7-3.2zm6.8 0A9 9 0 0 1 19.1 7h-2.3c-.3-1.2-.8-2.3-1.4-3.2zM4 9h2.8a16 16 0 0 0 0 6H4a9 9 0 0 1 0-6zm4.8 0H11v6H8.8a14 14 0 0 1 0-6zM13 9h2.2a14 14 0 0 1 0 6H13zm4.2 0H20a9 9 0 0 1 0 6h-2.8a16 16 0 0 0 0-6zM4.9 17h2.3c.3 1.2.8 2.3 1.4 3.2A9 9 0 0 1 4.9 17zm3.3 0H11v3.9c-1.2-.5-2.2-1.9-2.8-3.9zm4.8 0h2.8c-.6 2-1.6 3.4-2.8 3.9zm3.8 0h2.3a9 9 0 0 1-3.7 3.2c.6-.9 1.1-2 1.4-3.2z"/></svg>
        www.tabletrade.com
      </li>
    </ul>
    <address class="address">
      Door No.,Street Name<br>
      City Name, State Zip Code
    </address>
  </div>
</div>
</body>
</html>
```